Website for Excavator and Earthworks Company

We require a modern, sleek and practical website for our newly created earthworks/excavator business in Perth, Western Australia called Gullwind Stonecut Earthworks.

The website should have a modern, cutting edge feel but only needs to be relatively simplistic in it's layout and eventual functionality.

Some pages it should have would be Home, About, Projects and Contact Us.

Number of Pages Required

1 page

```html
<!DOCTYPE html>
<html lang="en">
<head>
<meta charset="utf-8">
<title>Gullwind Stonecut Earthworks</title>
<link href="https://fonts.googleapis.com/css2?family=Barlow:wght@400;500;600;700&family=Barlow+Condensed:wght@700;800&display=swap" rel="stylesheet">
<style>
:root{
  --lime:#c9dc1c;
  --lime-dark:#aebf10;
  --ink:#1b1d1f;
  --charcoal:#2a2c2e;
  --grey:#8a8d90;
  --light:#f2f2f0;
  --white:#ffffff;
  --photo-warm:linear-gradient(135deg,#6d6a5f,#c49a52 55%,#8a6a3a);
  --photo-sky:linear-gradient(160deg,#9fb4c4,#c8a45a 60%,#6a5a3e);
  --photo-site:linear-gradient(150deg,#b9c3c9,#8c8a78 55%,#5e5442);
}
*{box-sizing:border-box;margin:0;padding:0}
html,body{width:1200px;height:4028px;overflow:hidden}
body{font-family:"Barlow",Arial,sans-serif;color:var(--ink);background:var(--white);position:relative}
.display{font-family:"Barlow Condensed","Arial Narrow",sans-serif;font-weight:800;text-transform:uppercase;line-height:.95;letter-spacing:.5px}
.eyebrow{font-size:13px;font-weight:700;color:var(--lime);letter-spacing:1.5px;text-transform:uppercase}
.btn{display:inline-block;font-weight:700;font-size:14px;padding:12px 22px;border-radius:4px;text-decoration:none}
.btn-lime{background:var(--lime);color:var(--ink)}
.btn-dark{background:var(--ink);color:var(--white);border:1px solid #555}
.btn-outline{border:1.5px solid var(--ink);color:var(--ink);background:transparent}
.photo{position:absolute;background:var(--photo-warm)}
.abs{position:absolute}

/* nav */
.site-nav{position:absolute;top:0;left:0;width:1200px;height:64px;background:var(--ink);display:flex;align-items:center;padding:0 120px;z-index:5}
.brand{display:flex;align-items:center;gap:10px;color:var(--lime);font-weight:700;font-size:18px}
.brand-mark{width:26px;height:26px;background:var(--lime);border-radius:3px}
.nav-links{display:flex;gap:36px;margin-left:auto;margin-right:160px;list-style:none}
.nav-links a{color:var(--white);font-size:14px;text-decoration:none;font-weight:500}

/* hero */
.hero{position:absolute;top:0;left:0;width:1200px;height:600px;background:var(--ink);overflow:hidden}
.hero-photo{position:absolute;inset:0;background:linear-gradient(120deg,#3b3a36 30%,#8a6b3a 60%,#e0a34c 85%,#c87a30);clip-path:polygon(61% 0,100% 0,100% 100%,50% 100%)}
.hero-stripe{position:absolute;inset:0;background:var(--lime);clip-path:polygon(58% 0,60.5% 0,49.5% 100%,47% 100%)}
.hero-copy{position:absolute;left:144px;top:162px;width:400px}
.hero-copy h1{color:var(--white);font-size:62px;margin:14px 0 18px}
.hero-copy p{color:#d9d9d9;font-size:16px;font-weight:600;line-height:1.4;margin-bottom:24px}
.hero-copy .btn{margin-right:10px}

/* about */
.about{position:absolute;top:600px;left:0;width:1200px;height:560px}
.about .photo-back{left:130px;top:100px;width:250px;height:260px;background:var(--photo-sky)}
.about .photo-front{left:250px;top:220px;width:290px;height:260px;background:var(--photo-site);border:6px solid var(--white)}
.about .badge{left:340px;top:190px;width:70px;height:70px;border-radius:50%;background:var(--lime);border:5px solid var(--white)}
.about-copy{position:absolute;left:668px;top:105px;width:400px}
.about-copy h2{font-size:50px;margin:8px 0 20px}
.about-copy p{font-size:13px;line-height:1.55;color:#444;margin-bottom:14px}
.features{display:flex;gap:24px;margin:18px 0 26px}
.feature{display:flex;align-items:center;gap:10px;font-size:12px;font-weight:700;width:180px}
.feature-icon{width:36px;height:36px;border-radius:50%;background:var(--ink);flex:none}
.rule{position:absolute;top:1160px;left:120px;width:960px;height:2px;background:#d8d8d8}

/* services */
.services{position:absolute;top:1240px;left:0;width:1200px;height:700px;text-align:center}
.services .mark{width:40px;height:40px;background:var(--lime);border-radius:3px;margin:20px auto 14px}
.section-title{font-size:54px}
.section-sub{font-size:13px;color:#555;width:480px;margin:12px auto 0;line-height:1.45}
.cards{position:absolute;top:205px;left:120px;display:flex;gap:20px}
.card{width:306px;text-align:left}
.card .shot{height:310px;background:var(--photo-site)}
.card:nth-child(2) .shot{background:var(--photo-sky)}
.card:nth-child(3) .shot{background:var(--photo-warm)}
.card-body{background:var(--lime);padding:36px 22px 22px;position:relative;height:170px}
.card-icon{position:absolute;top:-30px;left:20px;width:56px;height:56px;border-radius:50%;background:var(--ink);border:4px solid var(--lime)}
.card-body h3{font-size:28px}
.card-body p{font-size:12px;line-height:1.4;margin:6px 0 10px}
.card-body a{font-size:12px;font-weight:700;color:var(--ink);text-decoration:none}

/* band */
.band{position:absolute;top:1968px;left:0;width:1200px;height:190px;background:var(--lime);overflow:hidden}
.band-dark{position:absolute;inset:0;background:var(--ink);clip-path:polygon(62% 0,100% 0,100% 100%,58% 100%)}
.band .machine{left:80px;top:10px;width:230px;height:170px;background:linear-gradient(160deg,#e7c23a,#2b2b2b)}
.band h3{position:absolute;left:360px;top:50px;font-size:32px;width:320px;color:var(--ink)}
.band-call{position:absolute;left:770px;top:72px;display:flex;align-items:center;gap:12px;color:var(--white)}
.band-call small{display:block;font-size:11px;font-weight:700;letter-spacing:1px}
.band-call strong{font-size:16px}
.call-icon{width:44px;height:44px;border-radius:50%;background:var(--white);display:flex;align-items:center;justify-content:center}
.band .btn{position:absolute;left:950px;top:74px}

/* gallery */
.gallery{position:absolute;top:2220px;left:0;width:1200px;height:640px;text-align:center}
.gallery .photo:nth-child(odd){background:var(--photo-sky)}
.gallery-cta{position:absolute;top:470px;width:1200px}
.gallery-cta h3{font-size:26px}
.gallery-cta p{font-size:12px;color:#555;margin:8px 0 16px}

/* contact */
.contact{position:absolute;top:2900px;left:0;width:1200px;height:700px;overflow:hidden;background:var(--white)}
.skyline{position:absolute;left:0;bottom:0;width:1200px;height:330px;background:linear-gradient(180deg,rgba(200,200,200,.25),#6b6d6f 60%,#3a3c3e)}
.contact-copy{position:absolute;left:120px;top:40px;width:470px}
.contact-copy h2{font-size:58px;margin:10px 0 16px}
.contact-copy p{font-size:13px;color:#444;line-height:1.5;margin-bottom:20px;width:320px}
.contact-item{display:flex;gap:12px;align-items:center;margin-bottom:16px;font-size:13px}
.contact-item b{display:block;font-size:13px}
.dot-icon{width:34px;height:34px;border-radius:50%;background:var(--lime);display:flex;align-items:center;justify-content:center;flex:none}
.quote{position:absolute;left:600px;top:32px;width:480px;height:450px;background:var(--lime);padding:36px 56px}
.quote h2{font-size:46px;margin-bottom:22px}
.field{background:var(--white);height:38px;border-radius:2px;margin-bottom:14px;font-size:12px;color:#666;padding:11px 12px}
.row{display:flex;gap:14px}.row .field{flex:1}
.field.tall{height:76px}
.quote .send{display:block;background:var(--ink);color:var(--white);text-align:center;font-weight:700;font-size:14px;padding:12px;border-radius:2px}

/* footer */
.site-footer{position:absolute;top:3600px;left:0;width:1200px;height:428px;background:var(--charcoal);color:#ddd}
.footer-brand{position:absolute;left:150px;top:100px;display:flex;align-items:center;gap:14px;color:var(--lime);font-weight:700;font-size:26px;width:280px;line-height:1.15}
.footer-brand .brand-mark{width:60px;height:60px;flex:none}
.footer-col{position:absolute;top:80px}
.footer-col h4{color:var(--lime);font-size:14px;font-weight:700;margin-bottom:14px;text-transform:uppercase}
.footer-col li{list-style:none;font-size:13px;margin-bottom:10px}
.footer-col .line{display:flex;gap:10px;align-items:center;margin-bottom:12px;font-size:12px}
.footer-col .line .dot-icon{width:28px;height:28px}
.footer-bottom{position:absolute;bottom:0;left:0;width:1200px;height:54px;border-top:1px solid #444;display:flex;align-items:center;justify-content:center;font-size:12px;color:#aaa}
</style>
</head>
<body>

<section class="hero">
  <div class="hero-photo" role="img" aria-label="Excavator working a site at sunset"></div>
  <div class="hero-stripe"></div>
  <div class="hero-copy">
    <div class="eyebrow">Gullwind Stonecut Earthworks</div>
    <h1 class="display">Moving Earth.<br>Building<br>Foundations.</h1>
    <p>Providing expert earthworks, excavation, and site preparation services with precision, safety, and efficiency.</p>
    <a class="btn btn-lime">Get A Free Quote</a><a class="btn btn-dark">View Our Work</a>
  </div>
</section>

<nav class="site-nav">
  <div class="brand"><span class="brand-mark"></span>Gullwind Stonecut</div>
  <ul class="nav-links"><li><a>Home</a></li><li><a>About</a></li><li><a>Projects</a></li><li><a>Contact Us</a></li></ul>
  <a class="btn btn-lime" style="padding:9px 18px;font-size:13px">Get A Free Quote</a>
</nav>

<section class="about">
  <div class="photo photo-back" role="img" aria-label="Yellow excavator on a worksite"></div>
  <div class="photo photo-front" role="img" aria-label="Bulldozer levelling ground"></div>
  <div class="abs badge"></div>
  <div class="about-copy">
    <div class="eyebrow">Welcome to Gullwind Stonecut Earthworks</div>
    <h2 class="display">Building Strong<br>Foundations</h2>
    <p>Based in Perth, Western Australia, Gullwind Stonecut Earthworks is a trusted excavation and earthmoving company specialising in residential, commercial, and civil projects. Our team of experienced professionals is dedicated to delivering exceptional results with precision and efficiency.</p>
    <p>We utilise the latest equipment and techniques to ensure your project is completed on time, within budget, and to the highest standards of safety and quality.</p>
    <div class="features">
      <div class="feature"><span class="feature-icon"></span>Modern Machinery &amp; Equipment</div>
      <div class="feature"><span class="feature-icon"></span>Residential, Commercial &amp; Civil Projects</div>
    </div>
    <a class="btn btn-outline" style="padding:9px 18px;font-size:12px">About Info</a>
  </div>
</section>
<div class="rule"></div>

<section class="services">
  <div class="mark"></div>
  <h2 class="display section-title">Our Earthworks Services</h2>
  <p class="section-sub">We provide reliable earthworks and site preparation services, delivering precision, safety, and efficiency across residential, commercial, and civil projects.</p>
  <div class="cards">
    <article class="card"><div class="shot" role="img" aria-label="Site crew in safety vests on a worksite"></div>
      <div class="card-body"><span class="card-icon"></span><h3 class="display">Site Preparation</h3><p>Clearing, grading, and levelling for residential and commercial developments.</p><a>Learn More ›</a></div></article>
    <article class="card"><div class="shot" role="img" aria-label="Excavator digging a trench"></div>
      <div class="card-body"><span class="card-icon"></span><h3 class="display">Excavation</h3><p>Precise digging for foundations, pools, trenches, and drainage systems.</p><a>Learn More ›</a></div></article>
    <article class="card"><div class="shot" role="img" aria-label="Excavator moving earth at dusk"></div>
      <div class="card-body"><span class="card-icon"></span><h3 class="display">Earthmoving</h3><p>Large-scale earth movement for construction, landscaping, and roadway projects.</p><a>Learn More ›</a></div></article>
  </div>
</section>

<section class="band">
  <div class="band-dark"></div>
  <div class="photo machine" role="img" aria-label="Yellow excavator"></div>
  <h3 class="display">Driving Progress<br>Through Dependable<br>Machinery</h3>
  <div class="band-call">
    <span class="call-icon"><svg width="20" height="20" viewBox="0 0 24 24"><path fill="#1b1d1f" d="M6.6 10.8a15 15 0 006.6 6.6l2.2-2.2c.3-.3.7-.4 1-.2 1.1.4 2.3.6 3.6.6.6 0 1 .4 1 1V20c0 .6-.4 1-1 1A17 17 0 013 4c0-.6.4-1 1-1h3.5c.6 0 1 .4 1 1 0 1.3.2 2.5.6 3.6.1.3 0 .7-.2 1z"/></svg></span>
    <div><small>GET QUICK SUPPORT</small><strong>08 6100 4421</strong></div>
  </div>
  <a class="btn btn-lime">Get A Free Quote</a>
</section>

<section class="gallery">
  <h2 class="display section-title" style="margin-top:32px">Our Work Gallery</h2>
  <p class="section-sub">View our work across residential, commercial, and civil projects, delivered with expertise and attention to detail.</p>
  <div class="photo" style="left:120px;top:180px;width:126px;height:190px" role="img" aria-label="Excavator on site"></div>
  <div class="photo" style="left:260px;top:140px;width:220px;height:130px" role="img" aria-label="Loader at work"></div>
  <div class="photo" style="left:260px;top:284px;width:220px;height:130px" role="img" aria-label="Digging a trench"></div>
  <div class="photo" style="left:494px;top:150px;width:206px;height:120px" role="img" aria-label="Excavator arm"></div>
  <div class="photo" style="left:494px;top:284px;width:206px;height:150px" role="img" aria-label="Excavator at sunset"></div>
  <div class="photo" style="left:716px;top:160px;width:220px;height:110px" role="img" aria-label="Machinery on site"></div>
  <div class="photo" style="left:716px;top:284px;width:220px;height:130px" role="img" aria-label="Earthmoving works"></div>
  <div class="photo" style="left:950px;top:180px;width:126px;height:220px" role="img" aria-label="Excavator close-up"></div>
  <div class="gallery-cta">
    <h3 class="display">Let's Get Your Project Moving</h3>
    <p>Expert earthworks services to get your project started the right way.</p>
    <a class="btn btn-lime">Get A Free Quote</a>
  </div>
</section>

<section class="contact">
  <div class="skyline" role="img" aria-label="Silhouette of construction machinery and city skyline"></div>
  <div class="contact-copy">
    <div class="eyebrow">Get in touch</div>
    <h2 class="display">Let's Talk About<br>Your Project</h2>
    <p>We'd love to help with your earthworks project. Reach out for honest advice and a free quote.</p>
    <div class="contact-item"><span class="dot-icon"><svg width="16" height="16" viewBox="0 0 24 24"><path fill="#1b1d1f" d="M12 2a7 7 0 00-7 7c0 5 7 13 7 13s7-8 7-13a7 7 0 00-7-7zm0 9.5A2.5 2.5 0 1112 6a2.5 2.5 0 010 5.5z"/></svg></span><div><b>Location</b>Perth, Western Australia</div></div>
    <div class="contact-item"><span class="dot-icon"><svg width="16" height="16" viewBox="0 0 24 24"><path fill="#1b1d1f" d="M6.6 10.8a15 15 0 006.6 6.6l2.2-2.2c.3-.3.7-.4 1-.2 1.1.4 2.3.6 3.6.6.6 0 1 .4 1 1V20c0 .6-.4 1-1 1A17 17 0 013 4c0-.6.4-1 1-1h3.5c.6 0 1 .4 1 1 0 1.3.2 2.5.6 3.6.1.3 0 .7-.2 1z"/></svg></span><div><b>Phone</b>08 6100 4421</div></div>
    <div class="contact-item"><span class="dot-icon"><svg width="16" height="16" viewBox="0 0 24 24"><path fill="#1b1d1f" d="M3 5h18v14H3zm2 2v.5l7 4.5 7-4.5V7z"/></svg></span><div><b>Email</b>hello@gullwindstonecut.com.au</div></div>
  </div>
  <form class="quote">
    <h2 class="display">Get A Free Quote</h2>
    <div class="field">Name</div>
    <div class="row"><div class="field">Email</div><div class="field">Phone</div></div>
    <div class="field">Select Services ▾</div>
    <div class="field tall">Your Project Details</div>
    <span class="send">Send Message</span>
  </form>
</section>

<footer class="site-footer">
  <div class="footer-brand"><span class="brand-mark"></span>Gullwind Stonecut<br>Earthworks</div>
  <div class="footer-col" style="left:460px"><h4>Quick Links</h4><ul><li>Home</li><li>About</li><li>Projects</li><li>Contact Us</li></ul></div>
  <div class="footer-col" style="left:660px"><h4>Our Services</h4><ul><li>Site Preparation</li><li>Excavation</li><li>Earthmoving</li></ul></div>
  <div class="footer-col" style="left:880px"><h4>Contact Info</h4>
    <div class="line"><span class="dot-icon"></span>Perth, Western Australia</div>
    <div class="line"><span class="dot-icon"></span>08 6100 4421</div>
    <div class="line"><span class="dot-icon"></span>hello@gullwindstonecut.com.au</div>
  </div>
  <div class="footer-bottom">© 2025 Gullwind Stonecut Earthworks. All rights reserved.</div>
</footer>

</body>
</html>
```